Re designing of website of VELTARO Pens, an International stationary brand

We would like to re design our existing website veltaropens.com. We are leading manufacturers and exporters of stationary products. Our existence is global -selling and marketing in all 5 continents.

We are a 35year old group with focus on high quality, innovative designs and state of art manufacturing setup.

Client satisfaction by committed service and trust are the roots of our organisation.

We would like to see a website which focuses on our brand Veltaro and must have an international appeal. Our target buyers would be Agents, distributors and wholesalers in various countries. Content would be similar to our existing website but designing and outlook needs to be totally different.

For the outlook we do like the following websites from our industry which can be used to draw inspiration.
1. www.quillbrookstationery.example
2. www.marovipen.example
3. www.tulsbergpen.example

The homepage need not be focused on the product but must emphasis on the branding of Veltaro, our existence of 35years along with international presence and quality standards maintained by our organisation.
Updates

Reason: Would like to see some more concepts and designs as per artwork attached.

Target Market(s)

Wholesalers, Agents and Distributors in all countries around the world. Target market is global

Number of Pages Required

1 page

Font styles to use
Sans Serif

Requirements
Must have
• Focus on Branding, High Quality Standards, Customer Loyalty
Nice to have
• Like the outlook of the websites
• www.tulsbergpen.example
• www.quillbrookstationery.example
• www.marovipen.example
Should not have
• Don't like the outlook of our present website www.veltaropens.com
• It doesn't justify our brand or our product

```html
<!DOCTYPE html>
<html lang="en">
<head>
<meta charset="utf-8">
<title>Veltaro – World Class Writing Instruments</title>
<link href="https://fonts.googleapis.com/css2?family=Roboto:wght@400;500&family=Roboto+Condensed:wght@400&family=Ubuntu:wght@500&family=Libre+Baskerville&display=swap" rel="stylesheet">
<style>
:root{
  --blue:#0d7fd4;
  --red:#e30613;
  --ink:#222;
  --muted:#555;
  --band:#efefef;
  --footer:#3b3b3b;
  --white:#fff;
}
*{margin:0;padding:0;box-sizing:border-box}
html,body{width:1200px;height:989px;overflow:hidden;background:var(--white)}
body{position:relative;font-family:"Roboto",sans-serif;color:var(--ink)}
.abs{position:absolute}

.topbar{left:0;top:0;width:1200px;height:41px;background:var(--blue)}
.topbar-rule{left:0;top:42px;width:1200px;height:2px;background:var(--red)}
.phone{left:782px;top:9px;display:flex;align-items:center;gap:8px;color:var(--white);font-size:17.5px}
.lang-sep{left:990px;top:0;width:1px;height:41px;background:rgba(255,255,255,.35)}
.lang{left:1002px;top:13px;color:var(--white);font-size:12px;font-weight:500}

.brand{left:161px;top:25px;width:307px;height:80px;background:var(--white);padding:6px}
.brand-inner{width:100%;height:100%;background:var(--red);display:flex;align-items:center;gap:10px;padding:0 12px}
.brand-square{width:44px;height:44px;background:var(--white)}
.brand-name{color:var(--white);font-family:"Roboto",sans-serif;font-weight:400;font-size:44px;letter-spacing:1px;line-height:1}

.nav{top:89px;display:flex;font-size:12.6px;color:#333;text-transform:uppercase}
.nav a{position:absolute;white-space:nowrap;color:inherit;text-decoration:none}
.header-rule{left:0;top:129px;width:1200px;height:1px;background:#ddd}

.hero{left:0;top:130px;width:1200px;height:397px;background:radial-gradient(ellipse at 20% 70%,#6a4a2e 0%,#2c3540 28%,#121820 55%,#050608 100%)}
.hero-copy{right:160px;top:262px;text-align:right;color:var(--white);font-family:"Ubuntu",sans-serif;font-weight:500;font-size:38px;line-height:56px}
.hero-arrow{top:307px;width:42px;height:35px;background:#3a3a3a;border:2px solid #888;display:flex;align-items:center;justify-content:center}
.hero-arrow.prev{left:0;border-left:none}
.hero-arrow.next{left:1154px;border-right:none}

.features{left:0;top:527px;width:1200px;height:177px;background:linear-gradient(90deg,#e9e9e9,#f7f7f7 50%,#e9e9e9)}
.feature{top:562px;width:154px;height:123px;border:1px solid #444;padding:4px;background:var(--white)}
.feature-inner{width:100%;height:100%;border:1px solid #444;display:flex;flex-direction:column;align-items:center;justify-content:flex-end;padding-bottom:7px}
.feature-art{margin-bottom:auto;margin-top:8px}
.feature-label{font-family:"Roboto Condensed",sans-serif;font-size:15.5px;color:#222;text-align:center;line-height:17px}

.welcome-title{left:0;top:729px;width:1200px;text-align:center;font-family:"Libre Baskerville",serif;font-size:19.5px;color:#333}
.welcome-rule{left:428px;top:763px}
.welcome-copy{left:180px;top:790px;width:840px;text-align:center;font-size:12.4px;line-height:22px;color:#333}
.more-rule{left:476px;top:881px;width:248px;height:1px;background:#ccc}
.more-btn{left:561px;top:870px;width:79px;height:24px;background:var(--red);color:var(--white);font-size:12.5px;display:flex;align-items:center;justify-content:center;border-radius:2px}

.footer{left:0;top:919px;width:1200px;height:66px;background:var(--footer)}
.footer-base{left:0;top:985px;width:1200px;height:4px;background:var(--blue)}
.footer-links{left:161px;top:932px;display:flex;font-size:12.4px;color:var(--white)}
.footer-links span{padding:0 11px;border-left:1px solid #777;line-height:14px}
.footer-links span:first-child{padding-left:0;border-left:none}
.copyright{left:161px;top:961px;font-size:11.4px;color:var(--white)}
.follow{left:793px;top:945px;font-size:11.4px;color:var(--white)}
.social{top:937px;width:28px;height:28px;border-radius:3px}
.social.s1{left:876px;background:#3b5998}
.social.s2{left:909px;background:#3fb0e8}
.social.s3{left:943px;background:#d9412f}
.footer-mark{left:988px;top:923px;width:52px;height:52px;background:var(--white);display:flex;align-items:center;justify-content:center;color:var(--red);font-size:10px;font-weight:500}
</style>
</head>
<body>

<div class="abs topbar"></div>
<div class="abs topbar-rule"></div>
<div class="abs phone">
  <svg width="22" height="22" viewBox="0 0 22 22"><circle cx="11" cy="11" r="10" fill="none" stroke="#fff" stroke-width="1.5"/><path d="M8 6c-1 1-1 3 1 6s4 4 5 4l1-2-2-1-1 1c-1-.5-2.5-2-3-3l1-1-1-2z" fill="#fff"/></svg>
  <span>(+00-11) 4820 7315</span>
</div>
<div class="abs lang-sep"></div>
<div class="abs lang">ENG &#709;</div>

<div class="abs brand">
  <div class="brand-inner">
    <div class="brand-square"></div>
    <div class="brand-name">VELTARO</div>
  </div>
</div>

<nav class="abs nav">
  <a style="left:494px">About Us</a>
  <a style="left:576px">Retail Products</a>
  <a style="left:706px">Promotional Products</a>
  <a style="left:886px">Careers</a>
  <a style="left:962px">Contact Us</a>
</nav>
<div class="abs header-rule"></div>

<section class="abs hero" role="img" aria-label="Businessman in a suit holding a glowing network of contact icons above his open hand"></section>
<h1 class="abs hero-copy">Creativity Is Thinking Up<br>New Things. Innovation Is<br>Doing New Things</h1>
<div class="abs hero-arrow prev"><svg width="10" height="14" viewBox="0 0 10 14"><path d="M8 1 2 7l6 6" fill="none" stroke="#fff" stroke-width="2.5"/></svg></div>
<div class="abs hero-arrow next"><svg width="10" height="14" viewBox="0 0 10 14"><path d="M2 1l6 6-6 6" fill="none" stroke="#fff" stroke-width="2.5"/></svg></div>

<div class="abs features"></div>
<div class="abs feature" style="left:175px"><div class="feature-inner">
  <div class="feature-art" role="img" aria-label="35 years of excellence badge, 1980 to 2015" style="width:80px;height:76px;background:#9a9a9a;border-radius:40px 40px 10px 10px"></div>
  <div class="feature-label">35year Old Group</div></div></div>
<div class="abs feature" style="left:348px"><div class="feature-inner">
  <div class="feature-art" role="img" aria-label="Handshake illustration" style="width:80px;height:52px;margin-top:16px;background:#333;border-radius:20px"></div>
  <div class="feature-label">Service And Trust</div></div></div>
<div class="abs feature" style="left:520px"><div class="feature-inner">
  <svg class="feature-art" width="70" height="70" viewBox="0 0 70 70"><circle cx="35" cy="35" r="33" fill="#bbb"/><circle cx="35" cy="35" r="24" fill="#e4e4e4"/></svg>
  <div class="feature-label">High Quality</div></div></div>
<div class="abs feature" style="left:693px"><div class="feature-inner">
  <svg class="feature-art" width="104" height="66" viewBox="0 0 104 66"><path d="M6 62l8-14 48-42 8 8-44 46z" fill="#222"/><path d="M44 62l4-16 40-40a6 6 0 0 1 8 8L56 54z" fill="none" stroke="#222" stroke-width="3"/></svg>
  <div class="feature-label">Innovative Designs</div></div></div>
<div class="abs feature" style="left:865px"><div class="feature-inner">
  <svg class="feature-art" width="50" height="60" viewBox="0 0 50 60" style="margin-top:2px"><path d="M26 6q4-4 8 0t8 0" fill="none" stroke="#222" stroke-width="2"/><rect x="36" y="14" width="7" height="26" fill="#222"/><path d="M4 56V34l10-6v6l10-6v6l10-6v6h10v22z" fill="#222"/><rect x="10" y="44" width="6" height="6" fill="#fff"/><rect x="22" y="44" width="6" height="6" fill="#fff"/><rect x="34" y="44" width="6" height="6" fill="#fff"/></svg>
  <div class="feature-label">State of Art<br>Manufacturing Setup</div></div></div>

<h2 class="abs welcome-title">Welcome to Veltaro</h2>
<svg class="abs welcome-rule" width="346" height="14" viewBox="0 0 346 14"><line x1="0" y1="1" x2="346" y2="1" stroke="#222"/><line x1="0" y1="4" x2="346" y2="4" stroke="#222"/><path d="M168 2l10 10M178 2l-10 10" stroke="#222"/></svg>
<p class="abs welcome-copy">Veltaro is one of India's largest manufacturers and exporters of writing instruments. Established in 1976, Veltaro has witnessed phenomenal growth over the last many years and now boast of customers across various segments in markets across the globe.Our commitment to developing new and original designs, creating innovative finishes and emphasis on complete customer satisfaction have been major catalysts.....</p>
<div class="abs more-rule"></div>
<div class="abs more-btn">Read More</div>

<footer class="abs footer"></footer>
<div class="abs footer-base"></div>
<div class="abs footer-links">
  <span>Home</span><span>About Us</span><span>Retail Products</span><span>Promotional Products</span><span>Careers</span><span>Contact Us</span>
</div>
<div class="abs copyright">Copyright ©2015, Veltaro.&nbsp; All Rights Reserved</div>
<div class="abs follow">Follow Us On</div>
<div class="abs social s1"></div>
<div class="abs social s2"></div>
<div class="abs social s3"></div>
<div class="abs footer-mark">VELTARO</div>

</body>
</html>
```